KRV Holdfast Manufacturer New Web Design

We need a new theme designed for metal fastener manufacturing company, KRV Holdfast Group, a $60M division of Benmore Forge Holdings, Inc. We manufacture screw, pins and washers to industrial customers (non-Automotive) such as Tallow Appliance, Marcus Fenwold, BRU, Veltrin, etc. Our current website is www.holdfastparts.example. We would like to stick with the same logo/color scheme, however, I'm aiming to modernize the website's look and feel.

Here are some of our competitor's websites:
- https://www.torvanix.example/
- http://quellbrook.example/
- http://www.morrowbuiltcouplingworks.example/
- http://pegsandoddments.example/
- http://www.dunmerebolting.example/

Target Market(s)

We primarily want to target engineers working in the following markets:
- Appliance (Tallow Appliance, Kelvanor)
- Ag (Fenwold, BRU)
- Recreational Vehicle (Veltrin, Briar Fox)
- Outdoor Power (Oldmeadow, Vexa)

We secondarily want to target buyers working at the above markets as well as buyers at Fastener distributors such as Boltrin, Provision Dynamics, Hollis Parfet.

Industry/Entity Type

Metal Forging

Number of Pages Required

1 page

Requirements
Must have
• For products: "Threaded" product as the primary focus. "Pins" product is the secondary focus, followed by all others.
• Please use same logo and color scheme as I do not plan to change.
Nice to have
• Highlight our featured proprietary products (pamphlets attached). KRV Holdfast's KIN-V, LumDrive, Holdfast Spiral, Pelmont.

```html
<!DOCTYPE html>
<html lang="en">
<head>
<meta charset="utf-8">
<title>KRV Holdfast Group</title>
<link href="https://fonts.googleapis.com/css2?family=Roboto:wght@400;500;700&display=swap" rel="stylesheet">
<style>
:root{
  --teal:#22cfa6;
  --blue:#5aaed8;
  --brand:#2aa3d8;
  --ink:#222;
  --muted:#666;
  --line:#e2e2e2;
  --black:#000;
  --panel:#efefef;
  --white:#fff;
}
*{box-sizing:border-box;margin:0;padding:0}
html,body{width:1200px;height:2423px;overflow:hidden}
body{font-family:'Roboto',Arial,sans-serif;color:var(--ink);background:var(--white);position:relative}
.wrap{position:absolute;left:199px;width:802px}
a{color:inherit;text-decoration:none}

/* header */
.top{position:absolute;top:0;left:0;width:1200px;height:94px;background:var(--white)}
.brand{position:absolute;left:199px;top:12px;display:flex;align-items:center;gap:8px}
.brand-dot{width:46px;height:46px;border-radius:50%;background:var(--brand)}
.brand-name{font-size:24px;font-weight:500;color:var(--brand)}
.contact{position:absolute;top:20px;display:flex;gap:10px;font-size:12px}
.contact .ico{width:30px;height:30px;border:1px solid var(--line);display:flex;align-items:center;justify-content:center}
.contact b{display:block;font-weight:500;color:var(--ink)}
.contact span{color:#999}
.nav{position:absolute;top:73px;left:199px;width:802px;height:42px;background:var(--black);display:flex;align-items:center;z-index:3}
.nav ul{list-style:none;display:flex;gap:22px;padding-left:21px;color:var(--white);font-size:12px;flex:1}
.nav .search{margin-right:54px}
.nav .quote{width:144px;height:42px;background:var(--blue);color:var(--white);font-size:12px;font-weight:500;display:flex;align-items:center;justify-content:center}

/* hero */
.hero{position:absolute;top:94px;left:0;width:1200px;height:508px;background:linear-gradient(120deg,#6f747a,#3e4247 55%,#5c6166)}
.hero h1{position:absolute;left:199px;top:157px;font-size:37px;font-weight:500;color:var(--white)}
.hero p{position:absolute;left:199px;top:214px;width:420px;font-size:13px;line-height:21px;color:var(--white)}
.btn{position:absolute;top:298px;height:48px;width:140px;display:flex;align-items:center;justify-content:center;color:var(--white);font-size:13px;font-weight:500}
.btn.teal{left:199px;background:var(--teal)}
.btn.blue{left:352px;background:var(--blue)}
.arrow{position:absolute;top:240px;width:40px;height:40px;border:2px solid var(--white);border-radius:50%}
.dots{position:absolute;top:437px;left:584px;display:flex;gap:4px}
.dots i{width:8px;height:8px;border-radius:50%;border:1px solid var(--white)}
.dots i.on{background:var(--teal);border-color:var(--teal)}

/* section titles */
.title{font-size:23px;font-weight:500;color:var(--ink)}
.title::after{content:"";display:block;width:40px;height:3px;background:var(--blue);margin-top:8px}

/* products */
.products{position:absolute;top:602px;left:0;width:1200px;height:339px}
.products .title{position:absolute;left:199px;top:58px}
.prod{position:absolute;top:133px;width:200px;text-align:center}
.prod .circ{width:64px;height:64px;border:1px solid #bbb;border-radius:50%;margin:0 auto;display:flex;align-items:center;justify-content:center}
.prod h3{font-size:13px;font-weight:500;margin-top:27px}
.prod p{font-size:11.5px;line-height:18px;color:var(--muted);margin-top:10px}

/* featured */
.featured{position:absolute;top:941px;left:0;width:1200px;height:522px;background:var(--panel)}
.featured .title{position:absolute;left:199px;top:66px}
.card{position:absolute;top:149px;width:194px;height:299px;background:var(--white)}
.card .ph{height:133px}
.card h4{font-size:10.5px;font-weight:500;padding:16px 10px 8px;border-bottom:1px solid var(--line)}
.card .desc{font-size:11px;line-height:16px;color:var(--muted);padding:6px 10px 0}
.card .feat{font-size:11.5px;font-weight:500;padding:9px 10px 4px}
.card ul{list-style:none;font-size:11px;line-height:17px;color:var(--muted);padding:0 10px}
.card .more{position:absolute;left:12px;bottom:-6px;width:68px;height:22px;background:var(--blue);color:var(--white);font-size:9.5px;display:flex;align-items:center;justify-content:center}

/* news */
.news{position:absolute;top:1463px;left:0;width:1200px;height:515px}
.news .title{position:absolute;left:199px;top:59px}
.post{position:absolute;top:126px;width:379px}
.post .ph{height:177px}
.post .date{position:absolute;top:34px/*below*/;}
.post .meta{display:flex;margin-top:22px}
.post .day{width:52px;text-align:center;font-size:19px;font-weight:500}
.post .day small{display:block;font-size:10px;font-weight:400}
.post .body{border-left:1px solid var(--line);padding-left:17px;width:260px}
.post h5{font-size:11.5px;font-weight:500;line-height:16px;letter-spacing:.3px}
.post .body p{font-size:11.5px;line-height:16px;color:var(--muted);margin-top:9px}
.post .read{display:block;margin-top:12px;font-size:11px;color:var(--blue)}

/* cta */
.cta{position:absolute;top:1978px;left:0;width:1200px;height:100px;background:var(--teal)}
.cta p{position:absolute;left:199px;top:26px;width:600px;font-size:15px;font-weight:500;line-height:24px;color:var(--white)}
.cta a{position:absolute;left:864px;top:28px;width:137px;height:46px;background:var(--white);color:var(--teal);font-size:13px;font-weight:500;display:flex;align-items:center;justify-content:center}

/* footer */
.footer{position:absolute;top:2078px;left:0;width:1200px;height:345px;background:var(--black);color:var(--white)}
.footer .brand{top:62px}
.footer .about{position:absolute;left:199px;top:138px;width:240px;font-size:11.5px;line-height:22px}
.social{position:absolute;left:199px;top:212px;display:flex;gap:18px}
.social i{width:10px;height:10px;border-radius:50%;background:var(--white)}
.footer h6{position:absolute;top:72px;font-size:12.5px;font-weight:700}
.links{position:absolute;top:135px;list-style:none;font-size:11.5px;line-height:24px}
.reach{position:absolute;left:767px;top:134px;list-style:none;font-size:11.5px;line-height:18px}
.reach li{display:flex;gap:14px;margin-bottom:10px}
.reach svg{flex:none;margin-top:2px}
.copy{position:absolute;left:0;bottom:0;width:1200px;height:60px;border-top:1px solid #333;display:flex;align-items:center;justify-content:center;font-size:11px}
</style>
</head>
<body>

<header class="top">
  <div class="brand"><span class="brand-dot"></span><span class="brand-name">KRV Holdfast group</span></div>
  <div class="contact" style="left:664px">
    <div class="ico"><svg width="14" height="10" viewBox="0 0 14 10"><rect x=".5" y=".5" width="13" height="9" fill="none" stroke="#999"/><path d="M.5 .5 7 6l6.5-5.5" fill="none" stroke="#999"/></svg></div>
    <div><b>E-mail :</b><span>sales@holdfastgroup.example</span></div>
  </div>
  <div class="contact" style="left:883px">
    <div class="ico"><svg width="12" height="12" viewBox="0 0 24 24"><path fill="#999" d="M6.6 10.8a15 15 0 0 0 6.6 6.6l2.2-2.2c.3-.3.7-.4 1-.2 1.1.4 2.3.6 3.6.6.6 0 1 .4 1 1V20c0 .6-.4 1-1 1A17 17 0 0 1 3 4c0-.6.4-1 1-1h3.5c.6 0 1 .4 1 1 0 1.3.2 2.5.6 3.6.1.3 0 .7-.2 1z"/></svg></div>
    <div><b>Call Us :</b><span>555-014-2652</span></div>
  </div>
</header>

<nav class="nav">
  <ul><li>Home</li><li>Products</li><li>Capabilities</li><li>Engineering</li><li>Quality</li><li>About Us</li><li>Contact/Quote Request</li></ul>
  <svg class="search" width="15" height="15" viewBox="0 0 16 16"><circle cx="6.5" cy="6.5" r="5" fill="none" stroke="#fff" stroke-width="2"/><path d="M10 10l5 5" stroke="#fff" stroke-width="2"/></svg>
  <a class="quote">GET A QUOTE</a>
</nav>

<section class="hero" role="img" aria-label="Close-up photograph of steel bolts, nuts and threaded rods">
  <span class="arrow" style="left:78px"><svg width="36" height="36" viewBox="0 0 36 36"><path d="M21 11l-7 7 7 7" fill="none" stroke="#fff" stroke-width="2"/></svg></span>
  <span class="arrow" style="left:1078px"><svg width="36" height="36" viewBox="0 0 36 36"><path d="M15 11l7 7-7 7" fill="none" stroke="#fff" stroke-width="2"/></svg></span>
  <h1>Better fasteners for Better Products</h1>
  <p>KRV Holdfast Group is a leading designer and manufacturer of value added, high quality engineered hardware solutions.</p>
  <a class="btn teal">READ MORE</a>
  <a class="btn blue">CONTACT US</a>
  <div class="dots"><i></i><i></i><i class="on"></i></div>
</section>

<section class="products">
  <h2 class="title">Our Products</h2>
  <div class="prod" style="left:187px">
    <div class="circ"><svg width="30" height="30" viewBox="0 0 30 30"><path d="M9 5h6M12 5v20M18 7h6M21 7v16" stroke="#555" stroke-width="2.5" fill="none"/></svg></div>
    <h3>THREADED</h3><p>KRV Holdfast Group has devel-<br>oped multiple screw..</p>
  </div>
  <div class="prod" style="left:396px">
    <div class="circ"><svg width="30" height="30" viewBox="0 0 30 30"><circle cx="15" cy="6" r="3" fill="none" stroke="#555" stroke-width="2"/><path d="M15 9v18" stroke="#555" stroke-width="2"/></svg></div>
    <h3>PINS</h3><p>Our Pin business is the traditional<br>Corrin Latch product line..</p>
  </div>
  <div class="prod" style="left:602px">
    <div class="circ"><svg width="30" height="30" viewBox="0 0 30 30"><circle cx="15" cy="15" r="11" fill="none" stroke="#555" stroke-width="2" stroke-dasharray="3 2"/><circle cx="15" cy="15" r="6" fill="none" stroke="#555" stroke-width="2"/></svg></div>
    <h3>STAMPINGS</h3><p>KRV Holdfast Group is the<br>largest, most diverse..</p>
  </div>
  <div class="prod" style="left:809px">
    <div class="circ"><svg width="30" height="30" viewBox="0 0 30 30"><circle cx="15" cy="13" r="8" fill="none" stroke="#555" stroke-width="3"/><path d="M10 24h10" stroke="#555" stroke-width="2"/></svg></div>
    <h3>LOCK WASHERS</h3><p>Historically, KRV Holdfast<br>Group's Helical Spring Lock</p>
  </div>
</section>

<section class="featured">
  <h2 class="title">Featured Proprietary Product</h2>
  <article class="card" style="left:199px">
    <div class="ph" role="img" aria-label="Photograph of trilobular thread-rolling screws" style="background:linear-gradient(135deg,#c9ccce,#707478)"></div>
    <h4>KIN-V THREAD-ROLLING SCREW</h4>
    <p class="desc">Trilobular screws typically require 40% more...</p>
    <p class="feat">Features</p><ul><li>→ Head styles</li><li>→ Point styles</li></ul>
    <a class="more">Read More</a>
  </article>
  <article class="card" style="left:402px">
    <div class="ph" role="img" aria-label="Photograph of bolts and nuts on wood" style="background:linear-gradient(135deg,#8a9aa6,#5b4438)"></div>
    <h4>LUMDRIVE</h4>
    <p class="desc">Dramatically advances fasten-ing performance</p>
    <p class="feat">Features</p><ul><li>→ Security</li><li>→ Engineered</li></ul>
    <a class="more">Read More</a>
  </article>
  <article class="card" style="left:605px">
    <div class="ph" role="img" aria-label="Photograph of a screwdriver driving a gold screw" style="background:linear-gradient(135deg,#c9a27a,#6e4e35)"></div>
    <h4>HOLDFAST SPIRAL</h4>
    <p class="desc">Controls loosening due to vibration, high heat...</p>
    <p class="feat">Features</p><ul><li>→ Anti-vibration</li><li>→ Engineered</li></ul>
    <a class="more">Read More</a>
  </article>
  <article class="card" style="left:807px">
    <div class="ph" role="img" aria-label="Photograph of blue zinc-plated screws" style="background:linear-gradient(135deg,#8fb2cf,#3f5f7e)"></div>
    <h4>PELMONT</h4>
    <p class="desc">Advances strip-out values and operating range</p>
    <p class="feat">Features</p><ul><li>→ Cost-savings</li><li>→ Efficiency</li></ul>
    <a class="more">Read More</a>
  </article>
</section>

<section class="news">
  <h2 class="title">News and Events</h2>
  <article class="post" style="left:199px">
    <div class="ph" role="img" aria-label="Photograph of blue bolts and nuts" style="background:linear-gradient(135deg,#9cc4e6,#2d6fb0)"></div>
    <div class="meta"><div class="day">25<small>Nov</small></div>
      <div class="body"><h5>KRV INTEGRATES LEADING MIDWEST FASTENER DIVISIONS</h5>
        <p>Effective immediately, Benmore Forge Holdings, a $16 billion diversified manufacturer of engineered products and specialty..</p>
        <a class="read">Read More →</a></div></div>
  </article>
  <article class="post" style="left:622px">
    <div class="ph" role="img" aria-label="Photograph of a brass wood screw" style="background:linear-gradient(135deg,#b8875a,#5a3a22)"></div>
    <div class="meta"><div class="day">25<small>Nov</small></div>
      <div class="body"><h5>KRV INTEGRATES LEADING MIDWEST FASTENER DIVISIONS</h5>
        <p>Effective immediately, Benmore Forge Holdings, a $16 billion diversified manufacturer of engineered products and specialty..</p>
        <a class="read">Read More →</a></div></div>
  </article>
</section>

<section class="cta">
  <p>KRV Holdfast Group always strives to improve our customer's products through designing and manufacturing value-added, quality solutions</p>
  <a>CONTACT US</a>
</section>

<footer class="footer">
  <div class="brand"><span class="brand-dot"></span><span class="brand-name">KRV Holdfast group</span></div>
  <p class="about">Known as KRV Holdfast Group today, the company is the result of a 2010 merger of KRV businesses that have a long…</p>
  <div class="social"><i></i><i></i><i></i><i></i></div>
  <h6 style="left:483px">INFORMATION</h6>
  <ul class="links" style="left:483px"><li>Home</li><li>Products</li><li>Capabilities</li><li>Engineering</li></ul>
  <ul class="links" style="left:603px"><li>Quality</li><li>About Us</li><li>Contact/Quote Request</li></ul>
  <h6 style="left:767px">GET IN TOUCH</h6>
  <ul class="reach">
    <li><svg width="12" height="12" viewBox="0 0 24 24"><path fill="#fff" d="M6.6 10.8a15 15 0 0 0 6.6 6.6l2.2-2.2c.3-.3.7-.4 1-.2 1.1.4 2.3.6 3.6.6.6 0 1 .4 1 1V20c0 .6-.4 1-1 1A17 17 0 0 1 3 4c0-.6.4-1 1-1h3.5c.6 0 1 .4 1 1 0 1.3.2 2.5.6 3.6.1.3 0 .7-.2 1z"/></svg><span>Phone : 555-014-2652</span></li>
    <li><svg width="12" height="14" viewBox="0 0 12 16"><path fill="#fff" d="M6 0a6 6 0 0 1 6 6c0 4-6 10-6 10S0 10 0 6a6 6 0 0 1 6-6zm0 3.5A2.5 2.5 0 1 0 6 8.5 2.5 2.5 0 0 0 6 3.5z"/></svg><span>Address : 410 S Quarry Avenue<br>Marlow Heights, IL 60999</span></li>
    <li><svg width="14" height="10" viewBox="0 0 14 10"><rect width="14" height="10" fill="#fff"/><path d="M0 0l7 6 7-6" fill="none" stroke="#000"/></svg><span>E-mail : sales@holdfastgroup.example</span></li>
  </ul>
  <div class="copy">© Copyright 2017 holdfast. All Rights Reserved.</div>
</footer>

</body>
</html>
```